The Merry Hound - Dog Training Business Card Design

I need a business card design for a new dog training company based in Cronulla NSW called The Merry Hound. I run puppy pre school classes, adult dog classes and do one on one training in the person's home.
I have studied for 2 years and use positive reinforcement training methods based on how dogs learn. I believe in communicating with our dogs what we want them to do rather than punish them for behaviours we don't like. I would like to see designs that use the colours that are used in my logo (please see attached)
I would like a simple and classic looking design. I don't want cartoon images of dogs or any animal images or drawings on the card. I have created my logo with this mindset. I am open to the subtle use of a dog's tail, paws or paw print.

Target Market(s)

high end area which is why I want a classic looking design
adults aged 25 and over

Industry/Entity Type

Dog Training

Contact Information for Business Card

Miriam Caslett
ORBIS Trained Professional Dog Trainer
www.themerryhound-example.com.au
0499731628
miriam@themerryhound-example.com.au

Font styles to use
Sans Serif

Colors
ffffff
86cae6
757575

Requirements
Must have
• Logo - I am trying to attach my logo and colour palette but it won't allow me. I will contact the company and upload ASAP.
Should not have
• images of dogs or cartoon drawings

```html
<!DOCTYPE html>
<html lang="en">
<head>
<meta charset="utf-8">
<title>The Merry Hound – Business Card</title>
<link href="https://fonts.googleapis.com/css2?family=Exo+2:wght@300;400;500;600&display=swap" rel="stylesheet">
<style>
  :root {
    --stage: #2f2f2f;
    --card-white: #f7f7f7;
    --brand-blue: #86cae6;
    --pale-blue: #b4d2ea;
    --brand-grey: #757575;
    --ink-white: #ffffff;
    --accent-orange: #e8773b;
    --text-font: "Exo 2", sans-serif;
  }
  * { box-sizing: border-box; margin: 0; padding: 0; }
  html, body { width: 1200px; height: 892px; overflow: hidden; }
  body { background: var(--stage); font-family: var(--text-font); position: relative; }

  .card { position: absolute; left: 260px; width: 680px; height: 389px; overflow: hidden; border-radius: 2px; }
  .card--back { top: 37px; background: var(--brand-grey); }
  .card--front { top: 466px; background: var(--card-white); }

  /* back face */
  .back-field { position: absolute; left: 0; top: 0; width: 100%; height: 300px; background: var(--pale-blue); display: flex; align-items: center; justify-content: center; }
  .back-web { position: absolute; left: 34px; bottom: 33px; color: var(--ink-white); font-size: 21px; font-weight: 500; letter-spacing: 0.5px; white-space: nowrap; }

  /* wordmark */
  .wordmark { display: flex; flex-direction: column; align-items: flex-start; }
  .wordmark-row { display: flex; align-items: center; gap: 12px; }
  .wordmark-name { font-size: 40px; font-weight: 300; color: var(--brand-grey); letter-spacing: 0.5px; line-height: 1; white-space: nowrap; }
  .wordmark-dot { flex: none; width: 18px; height: 18px; border-radius: 50%; background: var(--brand-blue); }
  .wordmark-tag { margin-top: 8px; font-size: 11px; font-weight: 400; letter-spacing: 2px; color: var(--brand-grey); text-transform: uppercase; white-space: nowrap; }
  .card--back .wordmark-name, .card--back .wordmark-tag { color: var(--ink-white); }
  .card--back .wordmark-dot { background: var(--brand-grey); }

  /* front face */
  .front-brand { position: absolute; left: 28px; top: 0; width: 250px; height: 240px; display: flex; align-items: center; }
  .front-brand .wordmark-row { gap: 8px; }
  .front-brand .wordmark-name { font-size: 27px; }
  .front-brand .wordmark-dot { width: 13px; height: 13px; }
  .front-brand .wordmark-tag { font-size: 8.5px; letter-spacing: 1.6px; }

  .contact-stack { position: absolute; left: 288px; top: 28px; width: 368px; display: flex; flex-direction: column; gap: 12px; }
  .name-panel { height: 108px; background: var(--brand-grey); border-radius: 10px; padding: 0 24px; display: flex; flex-direction: column; justify-content: center; }
  .name-panel__name { color: var(--ink-white); font-size: 27px; font-weight: 500; letter-spacing: 2px; line-height: 1.1; white-space: nowrap; }
  .name-panel__role { color: var(--accent-orange); font-size: 13px; font-weight: 500; letter-spacing: 0.6px; margin-top: 6px; white-space: nowrap; }

  .contact-row { display: flex; gap: 8px; height: 64px; }
  .contact-row__icon { flex: none; width: 56px; background: var(--pale-blue); border-radius: 8px; display: flex; align-items: center; justify-content: center; }
  .contact-row__icon svg { width: 22px; height: 22px; }
  .contact-row__text { flex: 1; min-width: 0; background: var(--pale-blue); border-radius: 8px; padding: 0 14px; display: flex; flex-direction: column; justify-content: center; color: var(--ink-white); font-size: 14px; font-weight: 500; letter-spacing: 0.5px; line-height: 1.5; white-space: nowrap; }
  .contact-row__text--web { font-size: 12.5px; letter-spacing: 0.3px; }
</style>
</head>
<body>

<section class="card card--back" aria-label="Business card, back">
  <div class="back-field">
    <div class="wordmark">
      <div class="wordmark-row">
        <span class="wordmark-name">The Merry Hound</span>
        <span class="wordmark-dot"></span>
      </div>
      <span class="wordmark-tag">positive dog training</span>
    </div>
  </div>
  <p class="back-web">www.themerryhound-example.com.au</p>
</section>

<section class="card card--front" aria-label="Business card, front">
  <div class="front-brand">
    <div class="wordmark">
      <div class="wordmark-row">
        <span class="wordmark-name">The Merry Hound</span>
        <span class="wordmark-dot"></span>
      </div>
      <span class="wordmark-tag">positive dog training</span>
    </div>
  </div>

  <div class="contact-stack">
    <div class="name-panel">
      <p class="name-panel__name">MIRIAM CASLETT</p>
      <p class="name-panel__role">ORBIS Trained Professional Dog Trainer</p>
    </div>

    <div class="contact-row">
      <div class="contact-row__icon">
        <svg viewBox="0 0 24 24" aria-hidden="true"><path d="M12 2a7 7 0 0 0-7 7c0 5 7 13 7 13s7-8 7-13a7 7 0 0 0-7-7zm0 9.5A2.5 2.5 0 1 1 12 6.5a2.5 2.5 0 0 1 0 5z" fill="#ffffff"/></svg>
      </div>
      <div class="contact-row__text">
        <span>14 Sample Parade</span>
        <span>Cronulla NSW 2230</span>
      </div>
    </div>

    <div class="contact-row">
      <div class="contact-row__icon">
        <svg viewBox="0 0 24 24" aria-hidden="true"><path d="M6.6 10.8a15.1 15.1 0 0 0 6.6 6.6l2.2-2.2a1 1 0 0 1 1-.25 11.4 11.4 0 0 0 3.6.57 1 1 0 0 1 1 1V20a1 1 0 0 1-1 1A17 17 0 0 1 3 4a1 1 0 0 1 1-1h3.5a1 1 0 0 1 1 1c0 1.25.2 2.45.57 3.57a1 1 0 0 1-.25 1z" fill="#ffffff"/></svg>
      </div>
      <div class="contact-row__text">
        <span>0499 731 628</span>
      </div>
    </div>

    <div class="contact-row">
      <div class="contact-row__icon">
        <svg viewBox="0 0 24 24" aria-hidden="true"><rect x="3" y="5" width="18" height="14" rx="2" fill="none" stroke="#ffffff" stroke-width="2"/><path d="M3.5 6.5 12 13l8.5-6.5" fill="none" stroke="#ffffff" stroke-width="2"/></svg>
      </div>
      <div class="contact-row__text contact-row__text--web">
        <span>miriam@themerryhound-example.com.au</span>
        <span>www.themerryhound-example.com.au</span>
      </div>
    </div>
  </div>
</section>

</body>
</html>
```